Can You Help Sell Glass Cabinets with a Banner Ad?

Our New Zealand-based company designs and sells glass cabinets and display cases. 75% of our customers are other businesses who want to display products in their shop or showroom. The other 25% of our customers are householders who want a glass cabinet for their personal collectables. We have been trading 2 years now, and are expanding rapidly. Our website address is www.vitrinaplace.example.nz.
We have made a strategic decision to focus on online advertising this year. This is because we want to raise our profile to the greatest number of and widest range of people. For now, this means banner advertising on high traffic New Zealand-based websites in an attempt to generate more traffic to our website. The websites we will initially use are www.ploverpost.example.nz and www.tuidaily.example.nz.
We therefore need a set of eye-catching banner ads designed for our online marketing campaign. The three banners required will probably just be variations on a single design.

Banner 1: Top Banner
760x120

Banner 2: Skyscraper
160x600

Banner 3: Medium Rectangle
300x250

Target Market(s)

The primary target market will be retailers who have shops and showrooms. They may not yet know they need a showcase.

Industry/Entity Type

Advertising

Requirements
Must have
• Vitrina Place logo
"High quality glass cabinets and showcases"
Maybe also "Show your products, not the cabinet"
[Corporate colour is green, as per logo. Secondary colours are orange, purple and grey.]
[Please use New Zealand (British) spelling]

Nice to have
• Please view our website and brochure on the Resources page for the look and feel of our company. In particular we like our logo, so it is possible you can take a lead from this. The logo emblem is designed to be evocative of glass.
The logo spot colour is 41,0,70,10.

```html
<!DOCTYPE html>
<html lang="en-NZ">
<head>
<meta charset="utf-8">
<title>Vitrina Place – Top Banner</title>
<link rel="stylesheet" href="https://fonts.googleapis.com/css2?family=Arimo:wght@400;700&display=swap">
<style>
  :root {
    --orange: #d4712a;
    --green: #8cc06d;
    --white: #ffffff;
    --cabinet-light: #f4f6f6;
    --cabinet-mid: #dde3e3;
    --page: #ffffff;
  }
  * { margin: 0; padding: 0; box-sizing: border-box; }
  html, body {
    width: 1200px;
    height: 189px;
    overflow: hidden;
    background: var(--page);
  }
  .banner {
    position: relative;
    width: 1200px;
    height: 189px;
    font-family: "Arimo", Arial, sans-serif;
    color: var(--white);
  }
  .headline-panel {
    position: absolute;
    left: 8px;
    top: 8px;
    width: 560px;
    height: 174px;
    background: var(--orange);
    border-radius: 34px 0 0 34px;
  }
  .headline {
    position: absolute;
    left: 86px;
    top: 14px;
    font-weight: 700;
    text-transform: uppercase;
    line-height: 1;
    letter-spacing: -0.5px;
  }
  .headline span { display: block; }
  .headline .line-1 { font-size: 53px; margin-bottom: 4px; }
  .headline .line-2,
  .headline .line-3 { font-size: 45px; margin-bottom: 4px; }
  .product-image {
    position: absolute;
    left: 538px;
    top: 0;
    width: 182px;
    height: 189px;
    background: linear-gradient(180deg, var(--cabinet-light) 0%, var(--cabinet-light) 60%, var(--cabinet-mid) 100%);
  }
  .accent-bar {
    position: absolute;
    left: 722px;
    top: 8px;
    width: 14px;
    height: 174px;
    background: var(--orange);
    border-radius: 0 8px 8px 0;
  }
  .tagline-panel {
    position: absolute;
    left: 757px;
    top: 5px;
    width: 435px;
    height: 180px;
    background: var(--green);
    border-radius: 28px;
  }
  .tagline {
    position: absolute;
    left: 36px;
    top: 30px;
    font-size: 19px;
    font-weight: 400;
  }
  .brand-name {
    position: absolute;
    left: 0;
    right: 0;
    top: 108px;
    text-align: center;
    font-size: 24px;
    font-weight: 700;
    text-transform: uppercase;
    letter-spacing: 0.5px;
    line-height: 1;
  }
</style>
</head>
<body>
  <div class="banner">
    <div class="headline-panel">
      <h1 class="headline">
        <span class="line-1">High Quality</span>
        <span class="line-2">Glass Cabinets</span>
        <span class="line-3">and Showcases</span>
      </h1>
    </div>
    <div class="product-image" role="img" aria-label="Photograph of a white-framed glass display cabinet with two glass shelves"></div>
    <div class="accent-bar"></div>
    <div class="tagline-panel">
      <p class="tagline">show your products, NOT THE CABINET</p>
      <p class="brand-name">Vitrina Place</p>
    </div>
  </div>
</body>
</html>
```